- Redesign our business card
- Logo remains unchanged
- Current business card attached

Target Market(s)

We are a property management company

Industry/Entity Type

Business

```html
<!DOCTYPE html>
<html lang="en">
<head>
<meta charset="utf-8">
<title>Harlow Property Group – Business Card</title>
<link rel="stylesheet" href="https://fonts.googleapis.com/css2?family=Open+Sans:wght@400;600&display=swap">
<style>
  :root {
    --card-grey: #b7b7b7;
    --panel-white: #ffffff;
    --olive: #827f44;
    --slate: #6b6c70;
    --ink: #111111;
    --text-light: #f4f4f4;
    --page: #ffffff;
  }
  html, body {
    margin: 0;
    padding: 0;
    background: var(--page);
    overflow: hidden;
  }
  .canvas {
    position: relative;
    width: 991px;
    height: 1200px;
    overflow: hidden;
    font-family: "Open Sans", Arial, sans-serif;
  }
  .card {
    position: absolute;
    left: 20px;
    width: 971px;
    background: var(--card-grey);
  }
  .card--front { top: 0; height: 587px; }
  .card--back  { top: 608px; height: 588px; }

  .front-panel {
    position: absolute;
    left: 0;
    top: 98px;
    width: 852px;
    height: 392px;
    background: var(--panel-white);
    border-radius: 0 51px 51px 0;
  }
  .brand-square {
    position: absolute;
    background: var(--olive);
  }
  .front-panel .brand-square {
    left: 95px;
    top: 120px;
    width: 150px;
    height: 150px;
  }
  .brand-name {
    position: absolute;
    left: 372px;
    top: 171px;
    margin: 0;
    font-size: 28px;
    font-weight: 400;
    color: var(--ink);
    letter-spacing: 0.3px;
    white-space: nowrap;
  }
  .brand-tagline {
    position: absolute;
    left: 390px;
    top: 205px;
    margin: 0;
    font-size: 17px;
    color: var(--olive);
    letter-spacing: 2.6px;
    white-space: nowrap;
  }

  .back-content {
    position: absolute;
    inset: 0;
    text-align: center;
    color: var(--text-light);
  }
  .card--back .brand-square {
    left: 425px;
    top: 46px;
    width: 120px;
    height: 120px;
  }
  .back-brand {
    position: absolute;
    left: 0; right: 0;
    top: 180px;
    margin: 0;
    font-size: 20px;
    font-weight: 400;
    color: var(--olive);
    letter-spacing: 1px;
  }
  .person-name {
    position: absolute;
    left: 0; right: 0;
    top: 262px;
    margin: 0;
    font-size: 28px;
    font-weight: 400;
    color: var(--text-light);
  }
  .person-title {
    position: absolute;
    left: 0; right: 0;
    top: 297px;
    margin: 0;
    font-size: 20px;
    color: var(--olive);
  }
  .contact {
    position: absolute;
    left: 0; right: 0;
    top: 372px;
    margin: 0;
    font-style: normal;
    font-size: 20px;
    line-height: 33.5px;
  }
  .contact span + span { margin-left: 14px; }
  .contact .web { margin-left: 20px; }
  .services {
    position: absolute;
    left: 0; right: 0;
    top: 536px;
    margin: 0;
    font-size: 22px;
  }
  .services .sep { margin: 0 8px; }
</style>
</head>
<body>
<main class="canvas">
  <section class="card card--front">
    <div class="front-panel">
      <div class="brand-square" aria-hidden="true"></div>
      <h1 class="brand-name">HARLOW PROPERTY GROUP</h1>
      <p class="brand-tagline">STRATA MANAGEMENT SERVICES</p>
    </div>
  </section>

  <section class="card card--back">
    <div class="back-content">
      <div class="brand-square" aria-hidden="true"></div>
      <p class="back-brand">HARLOW PROPERTY GROUP</p>
      <h2 class="person-name">DANIEL HARLOW</h2>
      <p class="person-title">Licensed Strata Manager</p>
      <address class="contact">
        PO BOX 48, MAPLE HILLS NSW 2090<br>
        12/6-20 ASHBY STREET FERNVALE NSW 2091<br>
        <span>T: 02 5550 0148</span><span>F: 02 5550 0276</span><span>M: 0400 555 318</span><br>
        <span>E: info@harlowproperty.example</span><span class="web">www.harlowproperty.example</span>
      </address>
      <p class="services">Strata Management<span class="sep">|</span>Community Management<span class="sep">|</span>Property Management</p>
    </div>
  </section>
</main>
</body>
</html>
```